Business Card Design

Please use the Logo for colors and styles, and create a business card using the following info:

Matthias Loeber
Web Developer

Loeber Solutions
+41 76 482 17 05
matthias@loeber-solutions.example
www.loeber-solutions.example

Download the logo at http://loeber-solutions.example/tl_files/loeber_solutions.zip

Thanks for your works!

```html
<!DOCTYPE html>
<html lang="en">
<head>
<meta charset="utf-8">
<title>Loeber Solutions – Business Card</title>
<link rel="stylesheet" href="https://fonts.googleapis.com/css2?family=Open+Sans:wght@400;600;700&display=swap">
<style>
  :root {
    --bg: #ecebe7;
    --card: #ffffff;
    --blue: #0a7cc4;
    --navy: #0b4a7a;
    --ink: #2b2b2b;
    --shadow: rgba(0, 0, 0, 0.18);
  }
  * { margin: 0; padding: 0; box-sizing: border-box; }
  html, body {
    width: 1200px;
    height: 686px;
    overflow: hidden;
    background: var(--bg);
    font-family: "Open Sans", Arial, sans-serif;
  }
  .stage {
    position: relative;
    width: 1200px;
    height: 686px;
  }
  .card {
    position: absolute;
    width: 525px;
    height: 300px;
    background: var(--card);
    box-shadow: 0 2px 6px var(--shadow);
    overflow: hidden;
  }
  .card--front { left: 60px; top: 146px; }
  .card--back  { left: 621px; top: 244px; }

  .brand-name {
    position: absolute;
    left: 0;
    right: 0;
    text-align: center;
    color: var(--navy);
    font-weight: 600;
    text-transform: uppercase;
    white-space: nowrap;
    letter-spacing: 0.5px;
  }
  .card--front .brand-name { top: 72px; font-size: 32px; line-height: 40px; }
  .card--back .brand-name  { top: 122px; font-size: 44px; line-height: 52px; }

  .contact {
    position: absolute;
    left: 0;
    right: 0;
    top: 154px;
    text-align: center;
    color: var(--ink);
  }
  .contact__title { font-size: 15px; line-height: 22px; }
  .contact__name { color: var(--blue); font-weight: 700; }
  .contact__divider {
    display: inline-block;
    width: 1px;
    height: 15px;
    background: var(--ink);
    margin: 0 8px 0 10px;
    vertical-align: -2px;
  }
  .contact__role { color: var(--navy); font-weight: 700; font-size: 13.5px; }
  .contact__lines { font-size: 13px; line-height: 22px; margin-top: 0; }
  .contact__item { display: inline-flex; align-items: center; gap: 2px; margin: 0 7px; }
  .contact__item svg { width: 12px; height: 12px; fill: var(--blue); }
  .contact__web {
    font-size: 13px;
    line-height: 22px;
    font-weight: 700;
    color: var(--navy);
    letter-spacing: 1.4px;
  }

  .band {
    position: absolute;
    left: 0;
    bottom: 0;
    width: 525px;
    height: 26px;
    display: block;
  }
  .band__light { fill: var(--blue); }
  .band__dark  { fill: var(--navy); }
</style>
</head>
<body>
<main class="stage">

  <section class="card card--front" aria-label="Business card front">
    <h1 class="brand-name">Loeber Solutions</h1>
    <div class="contact">
      <p class="contact__title">
        <span class="contact__name">Matthias Loeber</span><span class="contact__divider"></span><span class="contact__role">Web Developer</span>
      </p>
      <p class="contact__lines">
        <span class="contact__item">
          <svg viewBox="0 0 24 24" aria-hidden="true"><path d="M6.6 10.8a15.1 15.1 0 0 0 6.6 6.6l2.2-2.2c.3-.3.7-.4 1-.2 1.1.4 2.3.6 3.6.6.6 0 1 .4 1 1V20c0 .6-.4 1-1 1A17 17 0 0 1 3 4c0-.6.4-1 1-1h3.5c.6 0 1 .4 1 1 0 1.3.2 2.5.6 3.6.1.3 0 .7-.2 1z"/></svg>+41 76 482 17 05
        </span>
        <span class="contact__item">
          <svg viewBox="0 0 24 24" aria-hidden="true"><path d="M2 5h20v2l-10 6L2 7zm0 4.3 10 6 10-6V19H2z"/></svg>matthias@loeber-solutions.example
        </span>
      </p>
      <p class="contact__web">www.loeber-solutions.example</p>
    </div>
    <svg class="band" viewBox="0 0 525 26" preserveAspectRatio="none" aria-hidden="true">
      <polygon class="band__light" points="0,0 373,0 395,26 0,26"/>
      <polygon class="band__dark" points="383,0 525,0 525,26 405,26"/>
    </svg>
  </section>

  <section class="card card--back" aria-label="Business card back">
    <h2 class="brand-name">Loeber Solutions</h2>
    <svg class="band" viewBox="0 0 525 26" preserveAspectRatio="none" aria-hidden="true">
      <polygon class="band__dark" points="0,0 111,0 133,26 0,26"/>
      <polygon class="band__light" points="121,0 525,0 525,26 143,26"/>
    </svg>
  </section>

</main>
</body>
</html>
```